Velmint website

A clean uncluttered design that shows at glance that we are in the Media and design and publishing business.

We would like to see designs that use colours that show warmth and quality.

The website should show:
- products
- projects

These should be displaxed in spaces that we can add or interchanges with new products or projects.
Updates

Target Market(s)

Business and project managers and buyers and authors.

Industry/Entity Type

Business

Requirements
Must have
• Good colours. Not too strong, not weak, but reflecting quality.

```html
<!DOCTYPE html>
<html lang="en">
<head>
<meta charset="utf-8">
<title>Velmint — Media, Design &amp; Publishing</title>
<link href="https://fonts.googleapis.com/css2?family=Arimo:wght@400;700&display=swap" rel="stylesheet">
<style>
  :root {
    --sand: #f3deb0;
    --cream: #f5e8cc;
    --frame: #f6ead0;
    --teal: #7bbfa8;
    --teal-deep: #1d6b4c;
    --teal-text: #1f6a50;
    --mint: #58b394;
    --slate: #3f5a66;
    --slate-dark: #2f4650;
    --footer: #3c5763;
    --footer-text: #c9d6db;
    --footer-head: #e8eef0;
    --ink: #3d5663;
    --card-text: #2e4c6b;
    --why-head: #a08a5a;
    --why-text: #6b5d45;
    --divider: #e0c894;
    --social: #a9b1b3;
  }
  * { box-sizing: border-box; margin: 0; padding: 0; }
  html, body { width: 1200px; height: 1145px; overflow: hidden; }
  body {
    position: relative;
    background: var(--sand);
    font-family: "Arimo", Arial, sans-serif;
  }
  .abs { position: absolute; }

  /* Header */
  .brand { left: 27px; top: 24px; display: flex; align-items: center; gap: 12px; }
  .brand-mark { width: 40px; height: 40px; background: var(--slate); }
  .brand-name { font-size: 52px; font-weight: 700; color: var(--slate); letter-spacing: 1px; line-height: 1; }

  .search { left: 849px; top: 29px; width: 331px; height: 38px; display: flex; }
  .search-field {
    flex: 1; background: #f5e8cf; border: 1px solid #e6d3a8;
    font-size: 13px; color: #7b6a45; padding: 11px 14px;
  }
  .search-btn { width: 44px; background: var(--mint); display: flex; align-items: center; justify-content: center; }

  /* Navigation */
  .main-nav { left: 615px; top: 97px; width: 568px; height: 46px; background: var(--slate); display: flex; }
  .main-nav a {
    color: #dfe8ec; text-decoration: none; font-size: 19px; line-height: 46px;
    padding: 0 17px; letter-spacing: -0.3px;
  }
  .main-nav a.current { background: var(--slate-dark); color: #fff; padding: 0 17px; }

  /* Hero */
  .hero-band { left: 0; top: 143px; width: 1191px; height: 341px; background: var(--teal); }
  .hero-frame { left: 20px; top: 98px; width: 567px; height: 355px; background: var(--frame); padding: 11px; }
  .hero-photo {
    width: 100%; height: 100%;
    background: linear-gradient(180deg, #d9dcdf 0%, #c4c8cc 45%, #9a958e 60%, #6f6861 100%);
  }
  .hero-title { left: 622px; top: 186px; font-size: 42px; color: var(--teal-deep); letter-spacing: -0.5px; }
  .hero-text { left: 622px; top: 244px; width: 555px; font-size: 15.6px; line-height: 20.5px; color: var(--teal-text); }
  .read-more { left: 618px; top: 367px; width: 156px; height: 44px; display: flex; background: var(--slate); }
  .read-more .tip { width: 31px; background: var(--slate-dark); display: flex; align-items: center; justify-content: center; }
  .read-more span { color: #f3e6c8; font-size: 17px; line-height: 44px; padding-left: 17px; }

  /* Featured projects */
  .section-title { left: 16px; top: 510px; font-size: 41px; color: var(--ink); letter-spacing: -0.5px; }
  .project { top: 580px; width: 158px; }
  .project-thumb { width: 158px; height: 158px; }
  .project-text { margin-top: 12px; font-size: 14.2px; line-height: 17.8px; color: var(--card-text); }
  .project-arrow { margin-top: 14px; width: 21px; height: 21px; background: var(--slate); display: flex; align-items: center; justify-content: center; }
  .divider { top: 580px; width: 1px; height: 297px; background: var(--divider); }

  /* Why choose us */
  .why { left: 806px; top: 484px; width: 377px; height: 426px; background: var(--cream); padding: 47px 25px 0 24px; }
  .why h2 { font-weight: 400; font-size: 32px; color: var(--why-head); letter-spacing: -0.5px; margin-bottom: 16px; }
  .why p { font-size: 15.8px; line-height: 20.5px; color: var(--why-text); margin-bottom: 20px; }

  /* Footer */
  .site-footer { left: 0; top: 910px; width: 1200px; height: 235px; background: var(--footer); }
  .foot-head { top: 938px; font-size: 21px; color: var(--footer-head); }
  .foot-list { top: 980px; list-style: none; font-size: 14.5px; line-height: 17.8px; color: var(--footer-text); }
  .quote-text { left: 576px; top: 982px; width: 265px; font-size: 14.2px; line-height: 17.5px; color: var(--footer-text); }
  .quote-author { left: 571px; top: 1041px; font-size: 17px; color: #fff; }
  .social { top: 982px; width: 33px; height: 33px; border-radius: 50%; background: var(--social); }
  .newsletter { left: 922px; top: 1026px; font-size: 13px; line-height: 16.5px; color: #fff; }
  .subscribe { left: 921px; top: 1068px; width: 252px; height: 32px; display: flex; }
  .subscribe-field { flex: 1; background: #fff; font-size: 12.5px; color: #333; padding: 9px 12px; }
  .subscribe-btn { width: 87px; background: var(--mint); color: #fff; font-size: 14px; line-height: 32px; text-align: center; }
</style>
</head>
<body>

<header>
  <div class="abs brand">
    <div class="brand-mark"></div>
    <div class="brand-name">VELMINT</div>
  </div>
  <div class="abs search">
    <div class="search-field">search ...</div>
    <div class="search-btn">
      <svg width="24" height="24" viewBox="0 0 24 24"><circle cx="9" cy="9" r="6" fill="none" stroke="#fff" stroke-width="2.6"/><line x1="13.5" y1="13.5" x2="21" y2="21" stroke="#fff" stroke-width="3.4" stroke-linecap="round"/></svg>
    </div>
  </div>
</header>

<div class="abs hero-band"></div>

<nav class="abs main-nav">
  <a class="current" href="#">HOME</a>
  <a href="#">ABOUT</a>
  <a href="#">PRODUCTS</a>
  <a href="#">PROJECTS</a>
  <a href="#">CONTACT</a>
</nav>

<div class="abs hero-frame">
  <div class="hero-photo" role="img" aria-label="Photo of a young man sitting on a wooden deck working on a laptop under a cloudy sky"></div>
</div>

<h1 class="abs hero-title" style="font-weight:400">Lorem ipsum dolor sit amet elit</h1>
<p class="abs hero-text">Ut wisi enim ad minim veniam, quis nostrud exerci tation ullamcorper suscipit lobortis nisl ut aliquip ex ea commodo consequat. Duis autem vel eum iriure dolor in hendrerit in vulputate velit esse molestie consequat, vel illum dolore eu feugiat nulla facilisis at vero eros et accumsan et iusto odio dignissim qui blandit.</p>
<div class="abs read-more">
  <div class="tip"><svg width="8" height="8" viewBox="0 0 8 8"><polygon points="1,0 7,4 1,8" fill="#f3e6c8"/></svg></div>
  <span>Read more</span>
</div>

<h2 class="abs section-title" style="font-weight:400">Featured Projects</h2>

<div class="abs project" style="left:16px">
  <div class="project-thumb" role="img" aria-label="Stationery set with colourful flower branding" style="background:linear-gradient(135deg,#5a5e63,#d9dde0 50%,#6b6f74)"></div>
  <p class="project-text">Lorem ipsum dolor sit amet, consectetuer adipiscing elit, sed diam nonummy nibh euismod tincidunt .</p>
  <div class="project-arrow"><svg width="7" height="7" viewBox="0 0 8 8"><polygon points="1,0 7,4 1,8" fill="#fff"/></svg></div>
</div>
<div class="abs divider" style="left:193px"></div>

<div class="abs project" style="left:217px">
  <div class="project-thumb" role="img" aria-label="Set of brochure covers in green and purple" style="background:linear-gradient(135deg,#f4f4f2,#d7d3c6 40%,#a8487e 70%,#eeeeec)"></div>
  <p class="project-text">Lorem ipsum dolor sit amet, consectetuer adipiscing elit, sed diam nonummy nibh euismod tincidunt .</p>
  <div class="project-arrow"><svg width="7" height="7" viewBox="0 0 8 8"><polygon points="1,0 7,4 1,8" fill="#fff"/></svg></div>
</div>
<div class="abs divider" style="left:394px"></div>

<div class="abs project" style="left:416px">
  <div class="project-thumb" role="img" aria-label="Book cover with grey gears on a dark background" style="background:radial-gradient(circle at 55% 60%,#c9a23a 0%,#8e8e8e 25%,#2b2b2b 70%)"></div>
  <p class="project-text">Lorem ipsum dolor sit amet, consectetuer adipiscing elit, sed diam nonummy nibh euismod tincidunt .</p>
  <div class="project-arrow"><svg width="7" height="7" viewBox="0 0 8 8"><polygon points="1,0 7,4 1,8" fill="#fff"/></svg></div>
</div>
<div class="abs divider" style="left:595px"></div>

<div class="abs project" style="left:617px">
  <div class="project-thumb" role="img" aria-label="Brochure with a turquoise world map layout" style="background:linear-gradient(135deg,#ece8dc,#7fc2c4 45%,#d98a3a 75%,#e8e4d8)"></div>
  <p class="project-text">Lorem ipsum dolor sit amet, consectetuer adipiscing elit, sed diam nonummy nibh euismod tincidunt .</p>
  <div class="project-arrow"><svg width="7" height="7" viewBox="0 0 8 8"><polygon points="1,0 7,4 1,8" fill="#fff"/></svg></div>
</div>

<aside class="abs why">
  <h2>Why Choose Us?</h2>
  <p>Consectetuer adipiscing elit, sed diam nonummy nibh euismod tincidunt ut laoreet dolore magna aliquam erat volutpat. Ut wisi enim ad minim veniam, quis nostrud exerci tation ullamcorper suscipit lobortis nisl ut aliquip ex ea commodo consequat.</p>
  <p>Duis autem vel eum iriure dolor in hendrerit in vulputate velit esse molestie consequat, vel illum dolore eu feugiat nulla facilisis at vero eros et accumsan et iusto odio dignissim qui blandit praesent luptatum zzril delenit augue duis dolore te feugait nulla facilisi.</p>
</aside>

<footer>
  <div class="abs site-footer"></div>

  <h3 class="abs foot-head" style="left:26px;font-weight:400">Navigation</h3>
  <ul class="abs foot-list" style="left:26px">
    <li>Home</li><li>About</li><li>Products</li><li>Projects</li><li>Contact Us</li>
  </ul>

  <h3 class="abs foot-head" style="left:238px;font-weight:400">Products</h3>
  <ul class="abs foot-list" style="left:238px">
    <li>Media</li><li>Design</li><li>Publishing</li><li>Book Cover</li><li>Calling Cards</li>
  </ul>
  <ul class="abs foot-list" style="left:371px">
    <li>Brochure</li><li>Books</li><li>CD Cover</li><li>Branding</li>
  </ul>

  <h3 class="abs foot-head" style="left:504px;font-weight:400">Testimonial</h3>
  <svg class="abs" style="left:504px;top:980px" width="57" height="51" viewBox="0 0 57 51">
    <path d="M20 3 C9 3 2 10 2 18 C2 24 6 29 11 31 L8 40 L18 33 C19 33 20 33 20 33 C31 33 38 26 38 18 C38 10 31 3 20 3 Z" fill="none" stroke="#a9b8bf" stroke-width="3"/>
    <path d="M38 17 C47 17 54 23 54 30 C54 35 51 39 47 41 L49 49 L41 43 C40 43 39 43 38 43 C30 43 24 38 22 33" fill="none" stroke="#a9b8bf" stroke-width="3"/>
    <text x="13" y="24" font-family="Arimo, sans-serif" font-size="20" font-weight="700" fill="#a9b8bf">“</text>
    <text x="32" y="43" font-family="Arimo, sans-serif" font-size="20" font-weight="700" fill="#a9b8bf">”</text>
  </svg>
  <p class="abs quote-text">At vero eos et accusamus et iusto odio dignissimos ducimus, qui blanditiis praesentium voluptatum deleniti atque.</p>
  <p class="abs quote-author">- Dana Whitlow</p>

  <h3 class="abs foot-head" style="left:918px;font-weight:400">Connect with Us</h3>
  <div class="abs social" style="left:922px" aria-label="Social link"></div>
  <div class="abs social" style="left:966px" aria-label="Social link"></div>
  <div class="abs social" style="left:1010px" aria-label="Social link"></div>
  <div class="abs social" style="left:1054px" aria-label="Social link"></div>
  <div class="abs social" style="left:1098px" aria-label="Social link"></div>
  <p class="abs newsletter">subscribe to our monthly newsletter<br>and get the best deals and discounts</p>
  <div class="abs subscribe">
    <div class="subscribe-field">enter email</div>
    <div class="subscribe-btn">subscribe</div>
  </div>
</footer>

</body>
</html>
```